New Wix Website Design Project For New Finance Company

Create new design for a new page. Website should match existing theme of presentation deck, business card and logo attached to the brief. The site will have five pages

1) Home
2) Investment Criteria
3) Approach
4) Team
5) Contact

Some examples include
http://www.bluemaplefunds.com/

Although not a requirement, if the below white fence or similar could be added subtly to the sight as well, that would be great.

https://www.searvok.com/search?q=white+fence+horse&rlz=7K4TTPM_enUS218US264&source=lnms&tbm=isch&sa=X&ved=0bhVKEwqxmbtnyLvgBhWE3oNKHVtsBF4Q_BUIDyhD&biw=1920&bih=958#imgrc=vkd2PQx47eMLTA:

Target Market(s)

Business Professionals

Font styles to use
Sans Serif

Colors

Designer to choose colors to be used in the design.

Requirements
Must have
• Clean layout. Easy to upload header and footer.

```html
<!DOCTYPE html>
<html lang="en">
<head>
<meta charset="utf-8">
<title>Oak Ridge Capital</title>
<link rel="stylesheet" href="https://fonts.googleapis.com/css2?family=Poppins:wght@600&family=Raleway:wght@400;500;600;700&display=swap">
<style>
:root{
  --blue:#0a6cc0;
  --blue-deep:#0a5fae;
  --navy:#1b2a44;
  --ink:#262626;
  --muted:#666;
  --white:#fff;
  --footer:#060606;
}
*{margin:0;padding:0;box-sizing:border-box}
html,body{width:739px;height:1200px;overflow:hidden}
body{position:relative;font-family:"Raleway",sans-serif;background:var(--white);color:var(--ink)}
.abs{position:absolute}

/* header */
.site-header{top:0;left:0;width:739px;height:64px;background:var(--blue)}
.header-logo-bg{top:0;left:0}
.brand{left:47px;top:17px;color:var(--blue);font-weight:700;font-size:19px;letter-spacing:.5px;line-height:1.1}
.brand-sub{display:block;font-size:9px;letter-spacing:4px;font-weight:700;text-align:center}
.phone{right:61px;top:8px;color:var(--white);font-size:16px;font-weight:500;display:flex;align-items:center;gap:6px}
.main-nav{top:42px;right:0;display:flex;font-size:9.5px;color:var(--white);font-weight:500}
.main-nav a{color:inherit;text-decoration:none;margin-right:17px;padding:0 7px;height:22px;line-height:12px;display:block}
.main-nav a.is-active{border-bottom:2px solid var(--white)}
.nav-search{margin-right:46px;width:10px}

/* hero */
.hero{top:64px;left:0;width:739px;height:353px;background:linear-gradient(180deg,#3a4660 0%,#27344d 45%,#1c2538 75%,#2a3447 100%)}
.hero-title{top:118px;width:739px;text-align:center;font-family:"Poppins",sans-serif;font-weight:600;font-size:41px;color:var(--white);letter-spacing:.5px}
.hero-text{top:168px;left:150px;width:439px;text-align:center;color:var(--white);font-size:10.2px;line-height:17px}
.btn-slant{display:flex;align-items:center;justify-content:center;color:var(--white);font-weight:700;font-size:13px;text-decoration:none}
.hero-btn{top:217px;left:300px;width:138px;height:35px}
.hero-btn svg,.cta-btn svg{position:absolute;inset:0}
.hero-btn span,.cta-btn span{position:relative}

/* welcome */
.welcome{top:417px;left:0;width:739px;height:180px;background:var(--blue)}
.welcome-kicker{left:48px;top:68px;color:var(--white);font-weight:600;font-size:13px}
.welcome-title{left:45px;top:86px;color:var(--white);font-weight:600;font-size:27px}
.welcome-text{left:294px;top:48px;width:372px;color:var(--white);font-size:8.6px;line-height:16.8px}

/* approach */
.portrait{left:85px;top:640px;width:210px;height:326px;background:linear-gradient(180deg,#eef0f3 0%,#dfe3e8 55%,#2b2b2b 92%);border-radius:90px 90px 0 0}
.approach-title{left:341px;top:631px;color:var(--blue);font-weight:700;font-size:27px}
.feature-icon{left:337px;width:64px;height:64px;border-radius:50%;background:var(--blue);display:flex;align-items:center;justify-content:center}
.feature-name{left:428px;font-weight:600;font-size:12px;color:var(--ink)}
.feature-text{left:431px;width:225px;font-size:8.8px;line-height:16.8px;color:var(--muted)}

/* cta */
.cta{top:966px;left:0;width:739px;height:179px;background:linear-gradient(180deg,#1f6fba 0%,#0e66b8 50%,#1a6ab2 100%)}
.cta-title{top:38px;width:739px;text-align:center;color:var(--white);font-weight:600;font-size:22.5px;line-height:29px}
.cta-btn{top:104px;left:300px;width:139px;height:35px}

/* footer */
.site-footer{top:1145px;left:0;width:739px;height:55px;background:var(--footer)}
.footer-brand{left:47px;top:16px;color:var(--blue);font-weight:700;font-size:17px;line-height:1.05}
.footer-brand .brand-sub{font-size:8px;letter-spacing:3.5px}
.copyright{left:250px;top:22px;color:#ddd;font-size:8.6px}
.social{top:15px;width:26px;height:26px;border-radius:50%}
.social-a{left:607px;background:#3b5998}
.social-b{left:637px;background:#1da1f2}
.social-c{left:667px;background:#d34836}
</style>
</head>
<body>

<header class="site-header abs">
  <svg class="header-logo-bg abs" width="270" height="64" viewBox="0 0 270 64">
    <polygon points="0,0 270,0 234,64 0,64" fill="#9a9a9a"/>
    <polygon points="0,0 265,0 229,64 0,64" fill="#fff"/>
  </svg>
  <div class="brand abs">OAK RIDGE<span class="brand-sub">CAPITAL</span></div>
  <div class="phone abs">
    <svg width="18" height="18" viewBox="0 0 24 24" fill="#fff"><path d="M6.6 10.8a15.1 15.1 0 0 0 6.6 6.6l2.2-2.2c.3-.3.7-.4 1-.2 1.1.4 2.3.6 3.6.6.6 0 1 .4 1 1V20c0 .6-.4 1-1 1A17 17 0 0 1 3 4c0-.6.4-1 1-1h3.5c.6 0 1 .4 1 1 0 1.3.2 2.5.6 3.6.1.3 0 .7-.2 1z"/><path d="M14 2a8 8 0 0 1 8 8h-2a6 6 0 0 0-6-6zm0 4a4 4 0 0 1 4 4h-2a2 2 0 0 0-2-2z"/></svg>
    123 555 0147
  </div>
  <nav class="main-nav abs">
    <a href="#" class="is-active">HOME</a>
    <a href="#">INVESTMENT CRITERIA</a>
    <a href="#">APPROACH</a>
    <a href="#">TEAM</a>
    <a href="#">CONTACT</a>
    <svg class="nav-search" width="10" height="11" viewBox="0 0 10 11"><circle cx="4" cy="4" r="3" fill="none" stroke="#fff" stroke-width="1.8"/><line x1="6" y1="6.3" x2="9" y2="9.6" stroke="#fff" stroke-width="2"/></svg>
  </nav>
</header>

<section class="hero abs" role="img" aria-label="City skyline at dusk">
  <h1 class="hero-title abs">OAK RIDGE CAPITAL</h1>
  <p class="hero-text abs">Lorem Ipsum is simply dummy text of the printing and typesetting industry. Lorem Ipsum has been the industry's standard dummy text ever since the.</p>
  <a href="#" class="hero-btn btn-slant abs">
    <svg width="138" height="35" viewBox="0 0 138 35"><polygon points="10,0 138,0 128,35 0,35" fill="#0a6cc0"/></svg>
    <span>CONTACT US</span>
  </a>
</section>

<section class="welcome abs">
  <p class="welcome-kicker abs">WELCOME TO</p>
  <h2 class="welcome-title abs">OAK RIDGE</h2>
  <p class="welcome-text abs">Lorem Ipsum is simply dummy text of the printing and typesetting industry. Lorem Ipsum has been the industry's standard dummy text ever since the 1500s, when an unknown printer took a galley of type and scrambled it to make a type Lorem Ipsum is simply dummy text of the printing and typesetting industry. Lorem Ipsum has been the industry's standard dummy text ever since the 1500s, when an unknown printer.</p>
</section>

<div class="portrait abs" role="img" aria-label="Photo of a businesswoman holding a tablet"></div>
<h2 class="approach-title abs">OUR APPROACH</h2>

<div class="feature-icon abs" style="top:686px">
  <svg width="40" height="26" viewBox="0 0 40 26"><path d="M1 13C8 3 32 3 39 13 32 23 8 23 1 13z" fill="#fff"/><circle cx="20" cy="13" r="7" fill="#0a6cc0"/><circle cx="20" cy="13" r="3.5" fill="#fff"/></svg>
</div>
<h3 class="feature-name abs" style="top:688px">VISION</h3>
<p class="feature-text abs" style="top:707px">Lorem Ipsum is simply dummy text of the printing and typesetting industry Ipsum has been the.</p>

<div class="feature-icon abs" style="top:774px">
  <svg width="38" height="32" viewBox="0 0 38 32" fill="none" stroke="#fff" stroke-width="1.6"><polygon points="8,1 30,1 37,10 19,31 1,10" fill="#fff"/><polyline points="1,10 37,10" stroke="#0a6cc0"/><polyline points="13,1 10,10 19,31 28,10 25,1" stroke="#0a6cc0"/><polyline points="10,10 19,1 28,10" stroke="#0a6cc0"/></svg>
</div>
<h3 class="feature-name abs" style="top:782px">CORE VALUES</h3>
<p class="feature-text abs" style="top:801px">Lorem Ipsum is simply dummy text of the printing and typesetting industry Ipsum has been the.</p>

<div class="feature-icon abs" style="top:862px">
  <svg width="38" height="38" viewBox="0 0 38 38" fill="none" stroke="#fff" stroke-width="3"><circle cx="18" cy="20" r="15"/><circle cx="18" cy="20" r="9"/><circle cx="18" cy="20" r="3" fill="#fff"/><line x1="18" y1="20" x2="32" y2="6"/><polyline points="28,3 32,6 35,10" stroke-width="2.5"/></svg>
</div>
<h3 class="feature-name abs" style="top:868px;left:431px">MISSION</h3>
<p class="feature-text abs" style="top:887px">Lorem Ipsum is simply dummy text of the printing and typesetting industry Ipsum has been the.</p>

<section class="cta abs" role="img" aria-label="Countryside with a white wooden fence, tinted blue">
  <h2 class="cta-title abs">If You Need an Have any Question for<br>Contact Us Today !</h2>
  <a href="#" class="cta-btn btn-slant abs">
    <svg width="139" height="35" viewBox="0 0 139 35"><polygon points="11,0.5 138,0.5 128,34.5 1,34.5" fill="none" stroke="#fff" stroke-width="1"/></svg>
    <span>CONTACT US</span>
  </a>
</section>

<footer class="site-footer abs">
  <div class="footer-brand abs">OAK RIDGE<span class="brand-sub">CAPITAL</span></div>
  <p class="copyright abs">©SUMMIT CREST GROUP - 2019 All Rights Reserved.</p>
  <span class="social social-a abs" aria-label="Social link"></span>
  <span class="social social-b abs" aria-label="Social link"></span>
  <span class="social social-c abs" aria-label="Social link"></span>
</footer>

</body>
</html>
```